Redesign Of Flower Delivery Subscription Service Website

I need a revamped website of www.petal-tide.com

Please revamp current design using same content....

Target Market(s)

people who buy flowers. Brides, wedding planners, wedding photographer, married man, boyfriend, etc.

Industry/Entity Type

Florist

Number of Pages Required

5+ page

Colors

Designer to choose colors to be used in the design.

Requirements
Must have
• I need a revamped website of www.petal-tide.com
• Please revamp current design using same content....
Nice to have
Should not have

```html
<!DOCTYPE html>
<html lang="en">
<head>
<meta charset="utf-8">
<title>Petal Tide – Monthly Flower Delivery</title>
<link href="https://fonts.googleapis.com/css2?family=Lato:wght@300;400;700&family=Raleway:wght@400;500&display=swap" rel="stylesheet">
<style>
:root{
  --green:#8ccf4d;
  --green-dark:#6fb236;
  --ink:#2b2b2b;
  --text:#555;
  --muted:#8a8a8a;
  --panel:#ebebeb;
  --footer:#4a4a4a;
  --white:#fff;
}
*{margin:0;padding:0;box-sizing:border-box}
html,body{width:1200px;height:2913px;overflow:hidden;background:var(--white)}
body{position:relative;font-family:"Lato",sans-serif;color:var(--ink)}
.abs{position:absolute}
.btn{position:absolute;background:var(--green);color:var(--white);font-size:12px;letter-spacing:.5px;display:flex;align-items:center;justify-content:center;gap:8px;text-transform:uppercase}
.btn svg{width:12px;height:12px}

/* header */
.menu-icon{left:122px;top:36px;width:28px;height:18px}
.brand{left:522px;top:18px;width:180px;text-align:left}
.brand-name{font-family:"Raleway",sans-serif;font-size:34px;font-weight:400;color:var(--text);letter-spacing:1px;line-height:1}
.brand-tag{font-size:9px;color:var(--muted);margin-top:4px;padding-left:4px}
.header-icons{left:980px;top:38px;display:flex;gap:22px}
.header-icons svg{width:16px;height:16px}

/* hero */
.hero-panel{left:499px;top:0;width:701px;height:491px;background:var(--panel)}
.hero-title{left:122px;top:240px;font-family:"Raleway",sans-serif;font-size:48px;font-weight:400;letter-spacing:1px}
.hero-sub{left:122px;top:302px;font-size:14px;line-height:18px;color:var(--ink)}
.hero-sub b{font-weight:700;margin:0 8px 0 10px}
.hero-btn{left:208px;top:357px;width:171px;height:41px}
.hero-photo{left:548px;top:118px;width:620px;height:486px;border-radius:50% 40% 45% 50%/45% 50% 40% 55%;
  background:radial-gradient(ellipse at 35% 40%,#d8343f 0%,#c52a36 22%,#4d8a3a 48%,#2f6b2a 70%,rgba(235,235,235,0) 72%)}

/* services */
.services-title{left:0;top:665px;width:1200px;text-align:center;font-family:"Raleway",sans-serif;font-size:26px;letter-spacing:1px}
.services-band{left:0;top:831px;width:1200px;height:288px;background:var(--panel)}
.service{position:absolute;top:738px;width:226px;text-align:center}
.service-photo{width:226px;height:226px;border-radius:50%;border:8px solid var(--white);box-shadow:0 0 0 1px #ddd}
.service-name{margin-top:38px;font-family:"Raleway",sans-serif;font-size:18px;line-height:22px;letter-spacing:1px;color:#444}

/* subscription */
.bouquet-photo{left:0;top:1120px;width:581px;height:399px;background:radial-gradient(circle at 45% 50%,#f2f2ee 0%,#9fbf78 30%,#4c6b32 50%,#3a2d24 75%)}
.sub-title{left:617px;top:1190px;width:520px;font-family:"Raleway",sans-serif;font-size:28px;line-height:34px}
.sub-text{left:617px;top:1330px;width:470px;font-size:12px;line-height:16px;color:var(--text)}
.sub-btn{left:617px;top:1416px;width:169px;height:39px}

/* how it works */
.how-title{left:126px;top:1655px;font-family:"Raleway",sans-serif;font-size:26px}
.how-text{left:126px;top:1725px;width:260px;font-size:12px;line-height:16px;color:var(--text)}
.how-btn{left:124px;top:1847px;width:169px;height:39px}
.video{left:421px;top:1524px;width:779px;height:459px;background:linear-gradient(135deg,#cfcfcf,#bdbdbd);display:flex;align-items:center;justify-content:center}

/* newsletter */
.news-title{left:0;top:2082px;width:1200px;text-align:center;font-family:"Raleway",sans-serif;font-size:28px}
.news-form{left:270px;top:2150px;width:650px;height:58px;display:flex}
.news-input{flex:1;border:1px solid #999;font-size:12px;font-style:italic;color:var(--text);padding-left:20px;display:flex;align-items:center}
.news-btn{width:153px;background:var(--green);color:var(--white);font-size:12px;display:flex;align-items:center;justify-content:center}

/* perks */
.perk-band{left:0;top:2233px;width:1200px;height:350px;background:linear-gradient(180deg,#fff 0%,#f7c9d5 30%,#ef95ad 65%,#e7809c 100%)}
.perk{position:absolute;top:2402px;width:310px;height:82px;background:var(--white);border:1px solid #999;display:flex;align-items:center;padding-left:28px;gap:18px}
.perk svg{width:38px;height:38px;flex:none}
.perk h3{font-weight:400;font-size:18px;font-family:"Raleway",sans-serif}
.perk p{font-size:11px;line-height:13px;color:var(--muted)}

/* footer */
.footer{left:0;top:2583px;width:1200px;height:330px;background:var(--footer);color:var(--white)}
.f-col{position:absolute;top:52px}
.f-col h4{font-family:"Raleway",sans-serif;font-weight:500;font-size:27px;margin-bottom:12px}
.f-col p,.f-col li{font-size:12px;line-height:15px}
.f-col ul{list-style:none}
.f-col li::before{content:"•";margin-right:8px}
.contact-row{display:flex;gap:10px;margin-bottom:14px}
.contact-row svg{width:11px;height:11px;margin-top:2px;flex:none}
.socials{left:122px;top:205px;display:flex;gap:22px}
.socials span{width:12px;height:12px;border-radius:50%;background:var(--green)}
.socials span+span{background:#888}
.f-rule{left:122px;top:247px;width:962px;height:1px;background:#777}
.copy{left:122px;top:276px;font-size:11px}
.legal{left:897px;top:276px;font-size:11px}
</style>
</head>
<body>

<div class="abs hero-panel"></div>
<svg class="abs menu-icon" viewBox="0 0 28 18"><rect y="0" width="28" height="2.5" fill="#333"/><rect y="7" width="28" height="2.5" fill="#333"/><rect y="14" width="20" height="2.5" fill="#333"/></svg>
<div class="abs brand"><div class="brand-name">Petal Tide</div><div class="brand-tag">San Diego Flower Company</div></div>
<div class="abs header-icons">
  <svg viewBox="0 0 16 16"><circle cx="6.5" cy="6.5" r="4.5" fill="none" stroke="#333" stroke-width="2"/><line x1="10" y1="10" x2="14" y2="14" stroke="#333" stroke-width="2"/></svg>
  <svg viewBox="0 0 16 16"><circle cx="7" cy="5" r="3.5" fill="none" stroke="#333" stroke-width="1.8"/><path d="M1 15c0-4 12-4 12 0" fill="none" stroke="#333" stroke-width="1.8"/><circle cx="14" cy="12" r="2" fill="var(--green)"/></svg>
  <svg viewBox="0 0 16 16"><path d="M2 5h12l-1.5 9h-9z" fill="none" stroke="#333" stroke-width="1.8"/><path d="M5.5 5V3.5a2.5 2.5 0 0 1 5 0V5" fill="none" stroke="#333" stroke-width="1.6"/><circle cx="13" cy="12" r="2" fill="var(--green)"/></svg>
</div>

<div class="abs hero-photo" role="img" aria-label="Bunch of red tulips tied with a pink ribbon"></div>
<h1 class="abs hero-title">ALWAYS FRESH</h1>
<p class="abs hero-sub">Beautiful Flower Arrangements Delivered Monthly<br>Now only <b>$69.95/MTH</b>($100 value)</p>
<div class="btn hero-btn">Order Now <svg viewBox="0 0 12 12"><path d="M2 2l4 4-4 4M6 2l4 4-4 4" fill="none" stroke="#fff" stroke-width="1.5"/></svg></div>

<h2 class="abs services-title">OUR SERVICES</h2>
<div class="abs services-band"></div>
<div class="service" style="left:120px"><div class="service-photo" role="img" aria-label="Corporate table with pink floral centrepieces" style="background:radial-gradient(circle,#f4e4e0,#d9b5ad)"></div><div class="service-name">CORPORATE<br>ARRANGMENT</div></div>
<div class="service" style="left:361px"><div class="service-photo" role="img" aria-label="Hotel lounge with orchid arrangement" style="background:radial-gradient(circle,#f2d9c0,#c99a72)"></div><div class="service-name">HOTEL<br>ARRANGMENT</div></div>
<div class="service" style="left:609px"><div class="service-photo" role="img" aria-label="Event hall with tall white flower displays" style="background:radial-gradient(circle,#f0f2f0,#a8b5a8)"></div><div class="service-name">EVENTS<br>ARRANGMENT</div></div>
<div class="service" style="left:854px"><div class="service-photo" role="img" aria-label="Beach wedding arch decorated with purple flowers" style="background:linear-gradient(180deg,#cfe3ee,#e9e4ea 55%,#b88cb8)"></div><div class="service-name">WEDDING<br>ARRANGMENT</div></div>

<div class="abs bouquet-photo" role="img" aria-label="Bridal bouquet of white roses and green chrysanthemums"></div>
<h2 class="abs sub-title" style="font-weight:400">Monthly Subscription Based Flower Delivery Service in San Diego - CA by Our Florist Shop</h2>
<p class="abs sub-text">Every moment of life could be cherished perfectly.......IF you choose wisely. To make your day more treasured, remember that flowers are the smartest choice when delivered through our monthly PetalTide subscription based delivery service.</p>
<div class="btn sub-btn">Read More <svg viewBox="0 0 12 12"><path d="M2 2l4 4-4 4M6 2l4 4-4 4" fill="none" stroke="#fff" stroke-width="1.5"/></svg></div>

<h2 class="abs how-title" style="font-weight:400">HOW IT WORKS</h2>
<p class="abs how-text">PetalTide is a SET IT and FORGET IT subscription based flower delivery service. For an amazing price PetalTide will hand deliver a gorgeous arrangement directly to anyone, anywhere you want, every month.</p>
<div class="btn how-btn">Read More <svg viewBox="0 0 12 12"><path d="M2 2l4 4-4 4M6 2l4 4-4 4" fill="none" stroke="#fff" stroke-width="1.5"/></svg></div>
<div class="abs video" role="img" aria-label="Explainer video sketch of a couple dining and receiving a flower delivery">
  <svg width="72" height="72" viewBox="0 0 72 72"><circle cx="36" cy="36" r="34" fill="#333" opacity=".8"/><path d="M29 23l21 13-21 13z" fill="#fff"/></svg>
</div>

<h2 class="abs news-title" style="font-weight:400">Enter Your Email To Receive A Free Upgrade</h2>
<div class="abs news-form"><div class="news-input">Enter Your Email Address</div><div class="news-btn">SUBMIT NOW</div></div>

<div class="abs perk-band" role="img" aria-label="Pink gerbera daisies with palm leaves"></div>
<div class="perk" style="left:122px"><svg viewBox="0 0 38 38"><path d="M12 6h14l-2 6 5 8-3 14H12L9 20l5-8z" fill="var(--green)"/></svg><div><h3>FREE VASE</h3><p>Lorem Ipsum is simply dummy<br>text of the printing.</p></div></div>
<div class="perk" style="left:447px"><svg viewBox="0 0 38 38"><rect x="2" y="10" width="22" height="16" fill="var(--green)"/><path d="M24 15h7l5 6v5H24z" fill="var(--green)"/><circle cx="9" cy="29" r="4" fill="var(--green)" stroke="#fff" stroke-width="1.5"/><circle cx="29" cy="29" r="4" fill="var(--green)" stroke="#fff" stroke-width="1.5"/></svg><div><h3>FREE DELIVERY</h3><p>Lorem Ipsum is simply dummy<br>text of the printing.</p></div></div>
<div class="perk" style="left:771px"><svg viewBox="0 0 38 38"><path d="M19 3l14 15h-8v16H13V18H5z" fill="var(--green)"/></svg><div><h3>Free Upgrade</h3><p>Lorem Ipsum is simply dummy<br>text of the printing.</p></div></div>

<footer class="abs footer">
  <div class="f-col" style="left:122px;width:230px"><h4>ABOUT US</h4><p>Every moment of life could be cherished perfectly.......IF you choose wisely. To make your day more treasured.....</p></div>
  <div class="f-col" style="left:427px"><h4>QUICK LINK</h4><ul><li>Home</li><li>How it works</li><li>Delivery areas</li><li>Franchises</li><li>Corporate arrangments</li><li>Free flowers monthly</li><li>Blog</li><li>Contact</li></ul></div>
  <div class="f-col" style="left:654px"><h4>SERVICES</h4><ul><li>Corporate Arrangments</li><li>Hotel Arrangments</li><li>Events Arrangments</li><li>Wedding Arrangments</li></ul></div>
  <div class="f-col" style="left:880px;width:230px"><h4>QUICK LINK</h4>
    <div class="contact-row"><svg viewBox="0 0 12 12"><path d="M6 1a3.5 3.5 0 0 1 3.5 3.5C9.5 7 6 11 6 11S2.5 7 2.5 4.5A3.5 3.5 0 0 1 6 1z" fill="var(--green)"/></svg><p>1840 Harbor Crest Way El Cajon,<br>San Diego CA 92020</p></div>
    <div class="contact-row"><svg viewBox="0 0 12 12"><rect x="1" y="3" width="10" height="7" fill="var(--green)"/></svg><p>support@petaltidesd.com</p></div>
    <div class="contact-row"><svg viewBox="0 0 12 12"><path d="M3 1l2 3-1 1.5c.8 1.5 1.7 2.4 3 3L8.5 7l3 2-1 2C6 11 1 6 1 2z" fill="var(--green)"/></svg><p>619-555-0148</p></div>
  </div>
  <div class="abs socials"><span></span><span></span><span></span><span></span></div>
  <div class="abs f-rule"></div>
  <p class="abs copy">© Copyright 2018 Petal Tide - All Right Reserved</p>
  <p class="abs legal">Privacy Policy - Terms &amp; Conditions</p>
</footer>

</body>
</html>
```